Design for a real estate wev portal

Contents and features of the site
---------------------------------
Website in 5 languages: French, Dutch, English, German, Spanish.
English name of the site: Lantern Nest Living
Main purpose of the site:
- allow people to rent their house/ appartment for flatsharing purposes.
- help people wanting to find a room in flatsharing
- help people to find additional roommates for their flatsharing
Key interaction sequence:
1. I create a "group" of people who have common interest/hobbies
2. People who have the same interests/hobbies join my group
3. I look for a house/appartment to host my group
Website structure will be the following:
- Home
- Groups
-- Look for a group
--- Join a group
-- Create a group
- Properties
-- Look for a house/appartement
-- Apply
- Sales conditions
- Contact
- My account
-- My profile
-- My groups OR my properties
Your mission
------------
The client has no graphical guidelines, simply a logo (see attached).
We need a (responsive compliant) design for the following pages (we expect PSD's from you. No HTML nor CSS):
1. homepage (see example and wireframe attached)
2. properties search result list (see wireframe attached)
3. "detailed" form for properties
4. groups search result list
5. "detailed" form for groups
6. my account page
FOR THE COMPETITION step we only expect from you the design of first 2 screens.
Based on that, we will select the designer who will win the project, and will have to design the 4 remaining screens.
Target Market(s)
B2C
Industry/Entity Type
Real Estate
Number of Pages Required
5+ page
Look and feel
Each slider illustrates characteristics of the customer's brand and the style your logo design should communicate.

```html
<!DOCTYPE html>
<html lang="en">
<head>
<meta charset="utf-8">
<title>Lantern Nest Living — Home</title>
<link href="https://fonts.googleapis.com/css2?family=Ubuntu:wght@400;500;700&family=Open+Sans:wght@400;600;700&display=swap" rel="stylesheet">
<style>
:root{
  --blue:#3a9ad9;
  --blue-dark:#2f86c2;
  --green:#6cbd45;
  --green-dark:#5aa836;
  --ink:#2a2a2a;
  --muted:#555;
  --light:#f1f1f1;
  --dark:#262626;
  --darker:#141414;
  --line:#d9d9d9;
  --white:#fff;
}
*{box-sizing:border-box;margin:0;padding:0}
html,body{width:1200px;height:2857px;overflow:hidden}
body{font-family:"Open Sans",Arial,sans-serif;color:var(--ink);background:var(--white);font-size:12px;position:relative}
.wrap{width:876px;margin:0 auto;position:relative}
h1,h2,h3,h4{font-family:"Ubuntu","Open Sans",sans-serif;font-weight:500}

/* top bar */
.topbar{height:38px;background:var(--blue)}
.topbar .wrap{display:flex;align-items:center;height:38px;gap:8px}
.soc{width:19px;height:19px;border-radius:50%;background:var(--white)}
.soc.g{background:#bfe3a9}
.tb-btn{border:1px solid rgba(255,255,255,.55);color:#fff;font-size:11px;padding:4px 14px;border-radius:2px;background:var(--blue-dark)}
.tb-right{margin-left:auto;display:flex;gap:8px}

/* nav */
.nav{height:86px;background:#fff;border-bottom:1px solid #eee}
.nav .wrap{display:flex;align-items:center;height:86px;font-size:12px;color:#333}
.nav a{color:#333;text-decoration:none}
.nav .home{color:var(--blue);position:relative}
.nav .left,.nav .right{display:flex;gap:0;flex:1}
.nav .left a{margin-right:72px}
.nav .right{justify-content:flex-end}
.nav .right a{margin-left:46px}
.brand{position:absolute;left:50%;top:-26px;transform:translateX(-50%);width:220px;height:100px;background:#fff;display:flex;align-items:center;justify-content:center;gap:8px}
.brand .dot{width:14px;height:14px;border-radius:50%;background:var(--green)}
.brand span{font-family:"Ubuntu",sans-serif;font-weight:500;font-size:22px;color:#3d3d3d}

/* hero */
.hero{height:524px;position:relative;background:linear-gradient(135deg,#9aa3ab 0%,#8e979f 30%,#3a8fc8 48%,#2e83bf 70%,#8d969e 100%)}
.hero .map{position:absolute;inset:0}
.hero-copy{position:absolute;top:142px;left:0;right:0;text-align:center;color:#fff}
.hero-copy h1{font-size:35px;font-weight:700;letter-spacing:.5px;text-shadow:0 2px 3px rgba(0,0,0,.25)}
.hero-copy p{font-family:"Ubuntu",sans-serif;font-size:19px;margin-top:8px}
.hero-btns{display:flex;justify-content:center;gap:16px;margin-top:14px}
.btn{display:inline-flex;align-items:center;justify-content:center;color:#fff;font-size:12px;height:30px;padding:0 22px}
.btn.green{background:var(--green)}
.btn.blue{background:var(--blue)}
.arrow{position:absolute;top:170px}
.search{position:absolute;left:0;right:0;bottom:0;height:130px;background:rgba(40,40,40,.9)}
.search h2{text-align:center;color:#fff;font-size:22px;font-weight:500;padding-top:26px}
.search-row{display:flex;margin-top:17px;height:38px}
.search-row .field{flex:0 0 428px;background:#fff;display:flex;align-items:center;gap:8px;padding:0 12px;color:#666;font-size:11px}
.search-row .sel{background:#3b3b3b;border-left:1px solid #555;color:#ddd;font-size:11px;display:flex;align-items:center;justify-content:space-between;padding:0 10px}
.search-row .go{flex:0 0 48px;background:var(--blue);color:#fff;display:flex;align-items:center;justify-content:center;font-size:13px}
.notch{position:absolute;left:50%;bottom:-14px;transform:translateX(-50%);width:0;height:0;border-left:14px solid transparent;border-right:14px solid transparent;border-top:14px solid rgba(40,40,40,.9)}

/* choice panels */
.choices{padding-top:53px;height:403px}
.choices .wrap{display:flex;justify-content:space-between}
.panel{width:427px;height:297px;border:1px solid #a9d3ef}
.panel.alt{border-color:#b6df9f}
.panel-head{height:38px;background:var(--blue);color:#fff;display:flex;align-items:center;justify-content:space-between;padding:0 14px;font-family:"Ubuntu",sans-serif;font-size:17px}
.panel.alt .panel-head{background:var(--green)}
.pager{display:flex;gap:5px}
.pager i{width:16px;height:16px;border-radius:50%;background:#fff;display:block}
.panel-body{display:flex;justify-content:space-between;padding:16px 14px 0}
.tile{width:190px;text-align:center}
.photo{display:block;width:100%;background:linear-gradient(135deg,#cfc8bd,#8c8276)}
.tile .photo{height:130px}
.tile p{font-size:12px;line-height:17px;height:52px;margin-top:10px;color:#333}
.tile .btn{width:100%;justify-content:space-between;padding:0 14px;height:32px}

/* listings */
.listings{height:492px;background:linear-gradient(180deg,#2a2d31,#1d1f22 60%,#2f3236)}
.listings .wrap{display:flex;justify-content:space-between;padding-top:38px}
.col{width:427px}
.col-head{display:flex;justify-content:space-between;align-items:center;color:#fff;font-family:"Ubuntu",sans-serif;font-size:18px;padding-bottom:10px;border-bottom:1px solid #555;position:relative}
.col-head::after{content:"";position:absolute;left:24px;bottom:-7px;border-left:7px solid transparent;border-right:7px solid transparent;border-top:7px solid #555}
.item{background:#eee;height:134px;margin-top:30px;display:flex;padding:4px}
.item+.item{margin-top:30px}
.col .item:first-of-type{margin-top:20px}
.item .photo{width:148px;height:126px;flex:0 0 148px}
.item-info{padding:12px 14px;flex:1}
.item-top{display:flex;justify-content:space-between;font-family:"Ubuntu",sans-serif;font-size:14px}
.item-top .price{color:var(--green);font-size:15px}
.ticks{list-style:none;margin-top:8px}
.ticks li{display:flex;gap:7px;font-size:10.5px;line-height:14px;margin-bottom:5px;color:#555}
.ticks svg{flex:0 0 10px;margin-top:2px}
.col-foot{display:flex;justify-content:flex-end;margin-top:16px}
.col-foot .btn{width:168px;justify-content:space-between;height:33px;padding:0 14px}

/* features */
.features{height:552px}
.features .wrap{display:flex;justify-content:space-between;padding-top:40px}
.feat{width:424px}
.feat h3{color:var(--green);font-size:19px;font-weight:400}
.feat .photo{height:232px;margin-top:16px;border:4px solid #eee}
.feat .intro{font-size:11px;line-height:19px;color:#444;margin-top:20px}
.sep{height:1px;background:var(--line);margin:16px 0;position:relative}
.sep::before,.sep::after{content:"";position:absolute;top:-5px;width:9px;height:9px;border:1px solid var(--line);border-radius:50%;background:#fff}
.sep::before{left:0}.sep::after{right:0}
.feat h4{font-size:18px;color:#222}
.specs{display:grid;grid-template-columns:150px 110px 1fr;margin-top:10px;list-style:none}
.specs li,.benefits li{display:flex;gap:7px;font-size:10.5px;line-height:19px;color:#555}
.specs svg,.benefits svg{margin-top:5px;flex:0 0 10px}
.benefits{list-style:none;margin-top:10px}

/* faq */
.faq{height:496px;background:var(--light)}
.faq h2{text-align:center;color:var(--green);font-size:23px;padding-top:42px}
.faq-mark{display:block;margin:10px auto 16px}
.qa{background:#fff;border:1px solid #ddd;margin-bottom:19px}
.qa-head{display:flex;justify-content:space-between;align-items:center;height:38px;padding:0 14px;font-family:"Ubuntu",sans-serif;font-size:15px;color:#333}
.qa.open .qa-head{background:var(--blue);color:#fff}
.qa-body{padding:14px;font-size:10.5px;line-height:19px;color:#555}
.faq .more{display:flex;justify-content:flex-end}
.faq .more .btn{width:168px;justify-content:space-between;padding:0 14px}

/* footer */
.footer{height:228px;background:var(--dark);color:#ccc}
.footer .wrap{display:flex;padding-top:42px}
.footer h5{font-family:"Ubuntu",sans-serif;font-weight:400;font-size:17px;color:#fff;margin-bottom:14px}
.f-search{width:256px}
.f-search p{font-size:11px;font-weight:600;color:#fff}
.f-search .in{width:192px;height:36px;background:#fff;margin-top:14px;color:#555;font-size:10.5px;display:flex;align-items:center;padding:0 10px}
.f-search .btn{margin-top:8px;height:33px;font-size:12px}
.f-links{width:190px}
.f-links ul{list-style:none;font-size:10.5px;line-height:18.5px}
.f-links li::before{content:"•";margin-right:7px}
.f-info{width:230px;font-size:10.5px;line-height:18.5px}
.f-info .row{display:flex;gap:10px;margin-bottom:8px}
.f-brand{margin-left:auto;display:flex;align-items:center;gap:8px;padding-top:40px;height:120px}
.f-brand .dot{width:14px;height:14px;border-radius:50%;background:#777}
.f-brand span{font-family:"Ubuntu",sans-serif;font-weight:500;font-size:22px;color:#8a8a8a}
.bottombar{height:38px;background:var(--darker);color:#ddd;font-size:11px}
.bottombar .wrap{display:flex;align-items:center;height:38px}
.bottombar .icons{margin-left:auto;display:flex;gap:8px}
.bottombar .soc{background:#fff}
</style>
</head>
<body>

<header>
  <div class="topbar">
    <div class="wrap">
      <span class="soc"></span><span class="soc g"></span><span class="soc"></span>
      <span class="tb-btn">Create Your Group</span>
      <div class="tb-right">
        <span class="tb-btn">My Account</span>
        <span class="tb-btn">Login</span>
        <span class="tb-btn">English ⌄</span>
      </div>
    </div>
  </div>
  <nav class="nav">
    <div class="wrap">
      <div class="left">
        <a class="home">Home</a><a>Groups</a><a>Look For A Group</a>
      </div>
      <div class="brand"><i class="dot"></i><span>Lantern Nest Living</span></div>
      <div class="right">
        <a>Properties</a><a>Sales Conditions</a><a>Contact</a>
      </div>
    </div>
  </nav>
</header>

<section class="hero">
  <div class="map" role="img" aria-label="City map of a waterfront district with property location pins"></div>
  <svg class="arrow" style="left:62px" width="24" height="50" viewBox="0 0 24 50"><path d="M20 3 4 25l16 22" fill="none" stroke="rgba(255,255,255,.8)" stroke-width="2"/></svg>
  <svg class="arrow" style="right:62px" width="24" height="50" viewBox="0 0 24 50"><path d="M4 3l16 22L4 47" fill="none" stroke="rgba(255,255,255,.8)" stroke-width="2"/></svg>
  <div class="hero-copy">
    <h1>WE ARE REAL ESTATE HUB</h1>
    <p>FOR YOUR ALL NEEDS</p>
    <div class="hero-btns">
      <span class="btn green">Join A Group Today</span>
      <span class="btn blue">Contact Today</span>
    </div>
  </div>
  <div class="search">
    <div class="wrap">
      <h2>LOOK FOR A HOUSE/APPARTEMENT FOR RANT</h2>
      <div class="search-row">
        <div class="field">
          <svg width="12" height="12" viewBox="0 0 12 12"><circle cx="5" cy="5" r="3.8" fill="none" stroke="#777" stroke-width="1.5"/><path d="M8 8l3 3" stroke="#777" stroke-width="1.5"/></svg>
          Enter an address, town, Street, Zip, or Property ID
        </div>
        <div class="sel" style="flex:0 0 86px">All Cities <span>⇕</span></div>
        <div class="sel" style="flex:0 0 82px">All Areas <span>⇕</span></div>
        <div class="sel" style="flex:0 0 130px">Searching for rant <span>⇕</span></div>
        <div class="sel" style="flex:0 0 102px">⚙ &nbsp;Advanced</div>
        <div class="go">Go</div>
      </div>
    </div>
    <span class="notch"></span>
  </div>
</section>

<section class="choices">
  <div class="wrap">
    <article class="panel">
      <div class="panel-head">Searching For Accommodation <span class="pager"><i></i><i></i></span></div>
      <div class="panel-body">
        <div class="tile">
          <span class="photo" role="img" aria-label="Bright modern living room with white sofa"></span>
          <p>I want to Sale a Flat<br>Right Now !</p>
          <span class="btn blue">Contact Now <span>▸</span></span>
        </div>
        <div class="tile">
          <span class="photo" role="img" aria-label="Group of friends relaxing together on a sofa"></span>
          <p>I want to Join<br>a Group</p>
          <span class="btn blue">Contact Now <span>▸</span></span>
        </div>
      </div>
    </article>
    <article class="panel alt">
      <div class="panel-head">I Have a House for Rent <span class="pager"><i></i><i></i></span></div>
      <div class="panel-body">
        <div class="tile">
          <span class="photo" role="img" aria-label="Brick family house with front lawn"></span>
          <p>I want<br>to Advertise !</p>
          <span class="btn green">Contact Now <span>▸</span></span>
        </div>
        <div class="tile">
          <span class="photo" role="img" aria-label="Flatmates sitting on the floor sharing a meal"></span>
          <p>Why Is Flat Sharing<br>Interesting For Me ?</p>
          <span class="btn green">Contact Now <span>▸</span></span>
        </div>
      </div>
    </article>
  </div>
</section>

<section class="listings">
  <div class="wrap">
    <div class="col">
      <div class="col-head">For A Group <span class="pager"><i></i><i></i></span></div>
      <div class="item">
        <span class="photo" role="img" aria-label="Young flatmates talking at home"></span>
        <div class="item-info">
          <div class="item-top"><span>X1X Group</span><span class="price">150.00$</span></div>
          <ul class="ticks">
            <li><svg width="10" height="10" viewBox="0 0 10 10"><path d="M1 5l3 3 5-6" fill="none" stroke="#6cbd45" stroke-width="2"/></svg>Young workers, seeking for accomodation down town.</li>
            <li><svg width="10" height="10" viewBox="0 0 10 10"><path d="M1 5l3 3 5-6" fill="none" stroke="#6cbd45" stroke-width="2"/></svg>Average age: 35 Years</li>
            <li><svg width="10" height="10" viewBox="0 0 10 10"><path d="M1 5l3 3 5-6" fill="none" stroke="#6cbd45" stroke-width="2"/></svg>Men and Women welcome</li>
          </ul>
        </div>
      </div>
      <div class="item">
        <span class="photo" role="img" aria-label="Cosy shared living room interior"></span>
        <div class="item-info">
          <div class="item-top"><span>Pro Waa Group</span><span class="price">150.00$</span></div>
          <ul class="ticks">
            <li><svg width="10" height="10" viewBox="0 0 10 10"><path d="M1 5l3 3 5-6" fill="none" stroke="#6cbd45" stroke-width="2"/></svg>Young ladies, studying at University seeking for accomodation close to Brussels University.</li>
            <li><svg width="10" height="10" viewBox="0 0 10 10"><path d="M1 5l3 3 5-6" fill="none" stroke="#6cbd45" stroke-width="2"/></svg>Average age: 20 Years</li>
            <li><svg width="10" height="10" viewBox="0 0 10 10"><path d="M1 5l3 3 5-6" fill="none" stroke="#6cbd45" stroke-width="2"/></svg>Only Women</li>
          </ul>
        </div>
      </div>
      <div class="col-foot"><span class="btn blue">See More Groups <span>▸</span></span></div>
    </div>
    <div class="col">
      <div class="col-head">For A Houses <span class="pager"><i></i><i></i></span></div>
      <div class="item">
        <span class="photo" role="img" aria-label="Two-storey suburban house under blue sky" style="background:linear-gradient(180deg,#6fa4d8,#c9c6c0 60%,#6f9a55)"></span>
        <div class="item-info">
          <div class="item-top"><span>House</span><span class="price">1900.00$</span></div>
          <ul class="ticks">
            <li><svg width="10" height="10" viewBox="0 0 10 10"><path d="M1 5l3 3 5-6" fill="none" stroke="#777" stroke-width="2"/></svg>Town : Jackass Lane</li>
            <li><svg width="10" height="10" viewBox="0 0 10 10"><path d="M1 5l3 3 5-6" fill="none" stroke="#777" stroke-width="2"/></svg>3 BHK</li>
            <li><svg width="10" height="10" viewBox="0 0 10 10"><path d="M1 5l3 3 5-6" fill="none" stroke="#777" stroke-width="2"/></svg>Availability : Yes</li>
          </ul>
        </div>
      </div>
      <div class="item">
        <span class="photo" role="img" aria-label="Apartment living room with large windows"></span>
        <div class="item-info">
          <div class="item-top"><span>Appartment</span><span class="price">3900.00$</span></div>
          <ul class="ticks">
            <li><svg width="10" height="10" viewBox="0 0 10 10"><path d="M1 5l3 3 5-6" fill="none" stroke="#777" stroke-width="2"/></svg>Town : Mankato Blue Earth</li>
            <li><svg width="10" height="10" viewBox="0 0 10 10"><path d="M1 5l3 3 5-6" fill="none" stroke="#777" stroke-width="2"/></svg>2 BHK</li>
            <li><svg width="10" height="10" viewBox="0 0 10 10"><path d="M1 5l3 3 5-6" fill="none" stroke="#777" stroke-width="2"/></svg>Availability : Yes</li>
          </ul>
        </div>
      </div>
      <div class="col-foot"><span class="btn green">See More Houses <span>▸</span></span></div>
    </div>
  </div>
</section>

<section class="features">
  <div class="wrap">
    <div class="feat">
      <h3>Features For The Roommates</h3>
      <span class="photo" role="img" aria-label="Smiling roommates sharing a meal around a table" style="background:linear-gradient(135deg,#c79a6e,#8a5a3a)"></span>
      <p class="intro">Lorem ipsum dolor sit amet, consectetuer adipiscing elit, sed diam nonummy nibh euismod tincidunt ut laoreet dolore magna aliquam erat volutpat.</p>
      <div class="sep"></div>
      <h4>Property Details</h4>
      <ul class="specs">
        <li><svg width="10" height="10" viewBox="0 0 10 10"><path d="M1 5l3 3 5-6" fill="none" stroke="#6cbd45" stroke-width="2"/></svg>Property ID: HZ33</li>
        <li><svg width="10" height="10" viewBox="0 0 10 10"><path d="M1 5l3 3 5-6" fill="none" stroke="#6cbd45" stroke-width="2"/></svg>Bedrooms: 4</li>
        <li><svg width="10" height="10" viewBox="0 0 10 10"><path d="M1 5l3 3 5-6" fill="none" stroke="#6cbd45" stroke-width="2"/></svg>Garage Size: 200 SqFt</li>
        <li><svg width="10" height="10" viewBox="0 0 10 10"><path d="M1 5l3 3 5-6" fill="none" stroke="#6cbd45" stroke-width="2"/></svg>Price: $670.00</li>
        <li><svg width="10" height="10" viewBox="0 0 10 10"><path d="M1 5l3 3 5-6" fill="none" stroke="#6cbd45" stroke-width="2"/></svg>Bathrooms: 2</li>
        <li><svg width="10" height="10" viewBox="0 0 10 10"><path d="M1 5l3 3 5-6" fill="none" stroke="#6cbd45" stroke-width="2"/></svg>Year Built: 2016-01-09</li>
        <li><svg width="10" height="10" viewBox="0 0 10 10"><path d="M1 5l3 3 5-6" fill="none" stroke="#6cbd45" stroke-width="2"/></svg>Property Size: 1200 Sq Ft</li>
        <li><svg width="10" height="10" viewBox="0 0 10 10"><path d="M1 5l3 3 5-6" fill="none" stroke="#6cbd45" stroke-width="2"/></svg>Garage: 1</li>
      </ul>
      <div class="sep"></div>
    </div>
    <div class="feat">
      <h3>Features For The Owners</h3>
      <span class="photo" role="img" aria-label="Family standing in front of a large white house" style="background:linear-gradient(180deg,#e9eef2,#b9bcbf 55%,#6e9a4e)"></span>
      <p class="intro">Lorem ipsum dolor sit amet, consectetuer adipiscing elit, sed diam nonummy nibh euismod tincidunt ut laoreet dolore magna aliquam erat volutpat.</p>
      <div class="sep"></div>
      <h4>Benefits Details</h4>
      <ul class="benefits">
        <li><svg width="10" height="10" viewBox="0 0 10 10"><path d="M1 5l3 3 5-6" fill="none" stroke="#6cbd45" stroke-width="2"/></svg>It is a long established fact that a reader will be distracted by the readable.</li>
        <li><svg width="10" height="10" viewBox="0 0 10 10"><path d="M1 5l3 3 5-6" fill="none" stroke="#6cbd45" stroke-width="2"/></svg>Content of a page when looking at its layout.</li>
        <li><svg width="10" height="10" viewBox="0 0 10 10"><path d="M1 5l3 3 5-6" fill="none" stroke="#6cbd45" stroke-width="2"/></svg>The point of using Lorem Ipsum is that it has a more-or-less normal distribution.</li>
      </ul>
      <div class="sep"></div>
    </div>
  </div>
</section>

<section class="faq">
  <div class="wrap">
    <h2>Everything You Need To Know About Flatsharing</h2>
    <svg class="faq-mark" width="30" height="10" viewBox="0 0 30 10"><path d="M2 8l13-6 13 6" fill="none" stroke="#aaa" stroke-width="1.5" stroke-dasharray="3 2"/></svg>
    <div class="qa open">
      <div class="qa-head">Q1 ) Lorem Ipsum Dolor Sit Amet, Consectetur Adipiscing Elit, Sed Do Eiusmod Tempor Incidire Magna Aliqua.<span>−</span></div>
      <div class="qa-body">Sed ut perspiciatis unde omnis iste natus error sit voluptatem accusantium doloremque laudantium, totam rem aperiam, eaque ipsa quae ab illo inventore veritatis et quasi architecto beatae vitae dicta sunt explicabo. Nemo enim ipsam voluptatem quia voluptas sit aspernatur aut odit aut fugit, sed quia consequuntur magni dolores eos qui ratione voluptatem sequi nesciunt.</div>
    </div>
    <div class="qa"><div class="qa-head">Q2 ) &nbsp;But I must explain to you how all this mistaken idea of denouncing pleasure and praising<span>+</span></div></div>
    <div class="qa"><div class="qa-head">Q3 ) &nbsp;At vero eos et accusamus et iusto odio dignissimos ducimus qui blanditiis praesentium voluptatum.<span>+</span></div></div>
    <div class="qa"><div class="qa-head">Q4 ) &nbsp;Lorem Ipsum Dolor Sit Amet, Consectetur Adipiscing Elit, Sed Do E Labore Et Dolore Magna Aliqua.<span>+</span></div></div>
    <div class="more"><span class="btn green">See All Questions... <span>▸</span></span></div>
  </div>
</section>

<footer>
  <div class="footer">
    <div class="wrap">
      <div class="f-search">
        <h5>Quick Search</h5>
        <p>Lorem Ipsum Dolor Sit Amet Cons.</p>
        <div class="in">Enter an address, town,...</div>
        <span class="btn green">Search your home <span>&nbsp;▸</span></span>
      </div>
      <div class="f-links">
        <h5>Quick Links</h5>
        <ul><li>Home</li><li>Groups</li><li>Look For A Group</li><li>Properties</li><li>Sales Conditions</li><li>Contact</li></ul>
      </div>
      <div class="f-info">
        <h5>Quick Info</h5>
        <div class="row">
          <svg width="10" height="14" viewBox="0 0 10 14"><path d="M5 0a5 5 0 0 0-5 5c0 4 5 9 5 9s5-5 5-9a5 5 0 0 0-5-5z" fill="#aaa"/><circle cx="5" cy="5" r="1.8" fill="#262626"/></svg>
          <div>LANTERNNESTLIVING<br>Lorem Ipsum Dolor Sit Amet,<br>Conse.</div>
        </div>
        <div class="row">
          <svg width="11" height="11" viewBox="0 0 11 11"><path d="M2 0l2 2.5-1 1.5a7 7 0 0 0 4 4l1.5-1L11 9l-1.5 2C5 11 0 6 0 1.5z" fill="#aaa"/></svg>
          <div>+0123 456 789</div>
        </div>
        <div class="row">
          <svg width="12" height="9" viewBox="0 0 12 9"><rect width="12" height="9" fill="#aaa"/><path d="M0 0l6 5 6-5" fill="none" stroke="#262626"/></svg>
          <div>info@lanternnestliving.com</div>
        </div>
      </div>
      <div class="f-brand"><i class="dot"></i><span>Lantern Nest Living</span></div>
    </div>
  </div>
  <div class="bottombar">
    <div class="wrap">
      <span>© 2016 Lantern Nest Living. All Rights Reserved</span>
      <div class="icons"><span class="soc"></span><span class="soc g"></span><span class="soc"></span></div>
    </div>
  </div>
</footer>

</body>
</html>
```